Daniel Horvath Photography Business Card

I am a photographer in Philadelphia, PA. I have a business card that I have designed in Photoshop. This has been an ongoing process for me for far too long. I am 85% pleased with what I have. I need some experts like yourself who has that extra 25% to make this card 110%. I use the dots throughout my website as page/topic breaks. I also use the dots on the mailing side of my direct mail pieces.

Bluefield Printworks does my printing.
Their File Specs for a business card:
width - 3.625 inches
Height - 2.124 inches
@ 355 PPI or DPI
CMYK
1/8 inch Bleed/CUT
This is the size of my uploaded file samples

I will have the card printed on a 18 pt card stock - 4 color - 2 sides - with a matte coating

Tech Info: SIDE 01
For name DANIEL HORVATH : font choice is FoglihtenNo07 - size 14.4 - VA 150 - Text Height 140% - text width 130% - underlined - color is 30 - 30- 30 or (1e1e1e)
For word PHOTOGRAPHY : font choice is FoglihtenNo07 - size 6.4 - VA 360 - Text Height 200% - text width 270% - underlined - color is 162-162-162 or (a2a2a2)
For DOTS - font choice is FoglihtenNo07 - size 6.73 - VA 180 - Text Height 100% - text width 163% - color is 100-179-204 or (64b3cc) - blue dots / 1-1-1 or (010101) - Black dots
For DAN@DHORVATHSTUDIO.EXAMPLE - font choice is Helvetica Neue Light - size 4.55 - VA 121 - Text Height 200% - text width 132% - color is 1-1-1 or (010101)
For 555.418.7260 - font choice is Helvetica Neue Light - size 4.55 - VA 270 - Text Height 180% - text width 189% - color is 1-1-1 or (010101)
For DHORVATHSTUDIO.EXAMPLE - font choice is Helvetica Neue Light - size 9.1 - VA 180 - Text Height 150% - text width 130% - color is 133-192-214 or (85c0d6)

Tech Info: SIDE 02
not certain if it is my website address - DHORVATHSTUDIO.EXAMPLE - like the sample or
or my Logo with dots DANIEL HORVATH PHOTOGRAPHY, WITH UNDERLINEs AND DOTS JUST LIKE FIRST SIDE - MAYBE BIGGER
the name in Helvetica Neue Light - 255 pure white -
Dots are same colors as first side
The background color of choice - at least for now issssss: 84-91-99 or (545b63)

If you think you can make my card really say Wow! Please let me know. Thank you very much!

Target Market(s)

Ad Agencies

Industry/Entity Type

Professional Photography

Contact Information for Business Card

width - 3.625 inches
Height - 2.124 inches
@ 355 PPI or DPI
CMYK
1/8 inch Bleed/CUT

Tech Info: SIDE 01

Tech Info: SIDE 02

Font styles to use
Other font styles liked:
• FoglihtenNo07 and Helvetica Neue Light

Requirements
Must have
• I am a photographer in Philadelphia, PA. I have a business card that I have designed in Photoshop. This has been an ongoing process for me for far too long. I am 85% pleased with what I have. I need some experts like yourself who has that extra 25% to make this card 110%. I use the dots throughout my website as page/topic breaks. I also use the dots on the mailing side of my direct mail pieces.
• Bluefield Printworks does my printing.
• Their File Specs for a business card:
• width - 3.625 inches
• Height - 2.124 inches
• @ 355 PPI or DPI
• CMYK
• 1/8 inch Bleed/CUT
• This is the size of my uploaded file samples
• I will have the card printed on a 18 pt card stock - 4 color - 2 sides - with a matte coating
• Tech Info: SIDE 01
• For name DANIEL HORVATH : font choice is FoglihtenNo07 - size 14.4 - VA 150 - Text Height 140% - text width 130% - underlined - color is 30 - 30- 30 or (1e1e1e)
• For word PHOTOGRAPHY : font choice is FoglihtenNo07 - size 6.4 - VA 360 - Text Height 200% - text width 270% - underlined - color is 162-162-162 or (a2a2a2)
• For DOTS - font choice is FoglihtenNo07 - size 6.73 - VA 180 - Text Height 100% - text width 163% - color is 100-179-204 or (64b3cc) - blue dots / 1-1-1 or (010101) - Black dots
• For DAN@DHORVATHSTUDIO.EXAMPLE - font choice is Helvetica Neue Light - size 4.55 - VA 121 - Text Height 200% - text width 132% - color is 1-1-1 or (010101)
• For 555.418.7260 - font choice is Helvetica Neue Light - size 4.55 - VA 270 - Text Height 180% - text width 189% - color is 1-1-1 or (010101)
• For DHORVATHSTUDIO.EXAMPLE - font choice is Helvetica Neue Light - size 9.1 - VA 180 - Text Height 150% - text width 130% - color is 133-192-214 or (85c0d6)
• Tech Info: SIDE 02
• not certain if it is my website address - DHORVATHSTUDIO.EXAMPLE - like the sample or
• or my Logo with dots DANIEL HORVATH PHOTOGRAPHY, WITH UNDERLINEs AND DOTS JUST LIKE FIRST SIDE - MAYBE BIGGER
• the name in Helvetica Neue Light - 255 pure white -
• Dots are same colors as first side
• The background color of choice - at least for now issssss: 84-91-99 or (545b63)
• If you think you can make my card really say Wow! Please let me know. Thank you very much!
Nice to have
• I could really use some different sizes of the dots as a Vector file?? I use Photoshop for all my designs. Thank You.
Should not have
• all listed above

```html
<!DOCTYPE html>
<html lang="en">
<head>
<meta charset="utf-8">
<title>Daniel Horvath Photography – Business Card</title>
<link rel="stylesheet" href="https://fonts.googleapis.com/css2?family=Roboto:wght@300&display=swap">
<style>
  :root {
    --stage: #eeeeee;
    --card-front: #ffffff;
    --name-blue: #1d6cae;
    --text-grey: #555a5e;
    --back-center: #1bb3cb;
    --back-edge: #3354a4;
    --white: #ffffff;
  }
  html, body {
    margin: 0;
    width: 1200px;
    height: 469px;
    overflow: hidden;
    background: var(--stage);
    font-family: "Roboto", "Helvetica Neue", Arial, sans-serif;
    font-weight: 300;
  }
  .canvas {
    position: relative;
    width: 1200px;
    height: 469px;
  }
  .card {
    position: absolute;
    top: 107px;
    width: 433px;
    height: 254px;
  }
  .card--front {
    left: 110px;
    background: var(--card-front);
  }
  .card--back {
    left: 657px;
    background: radial-gradient(ellipse 62% 70% at 50% 50%, var(--back-center) 0%, var(--back-edge) 100%);
  }
  .studio-name {
    position: absolute;
    left: 0;
    right: 0;
    top: 117px;
    margin: 0;
    text-align: center;
    font-size: 18px;
    line-height: 24px;
    font-weight: 300;
    color: var(--name-blue);
  }
  .phone {
    position: absolute;
    left: 0;
    right: 0;
    top: 293px;
    top: 186px;
    text-align: center;
    font-size: 14px;
    line-height: 20px;
    letter-spacing: 0.3px;
    color: var(--text-grey);
  }
  .email {
    position: absolute;
    left: 0;
    right: 0;
    top: 117px;
    text-align: center;
    font-size: 14px;
    line-height: 20px;
    letter-spacing: 0.1px;
    color: var(--white);
  }
</style>
</head>
<body>
  <main class="canvas">
    <section class="card card--front" aria-label="Card front">
      <h1 class="studio-name">Daniel Horvath Photography</h1>
      <div class="phone">555.418.7260</div>
    </section>
    <section class="card card--back" aria-label="Card back">
      <div class="email">dan@dhorvathstudio.example</div>
    </section>
  </main>
</body>
</html>
```